Shopping centre customer engagement software website

We need a multi page site with :

*What we do.
*How it works.
*Benefits
* Case study
* Testimonial
* Business login (we provide link to business portal)
* Consumer login (we provide link to consumer site)
* Book a demo
* Contact us

We want it to be clean and crisp and very self explanatory with little clutter. We are thinking white but are open to what ever looks the best.
Updates

Wordpress is preferred

Target Market(s)

Shopping centre managers and retail property companies

Coding

Coded - Design and coding required

Number of Pages Required

5+ page

Font styles to use
Sans Serif

Colors
ffffff

Requirements
Must have
• As listed above and must be responsive! Checkout our existing site for the text to be included (will be edited but it’ll give you an idea) www.tovrendix.com

```html
<!DOCTYPE html>
<html lang="en">
<head>
<meta charset="utf-8">
<title>Tovrendix — Shopping Centre Engagement</title>
<link href="https://fonts.googleapis.com/css2?family=Raleway:wght@200;300;400;600;700&family=Open+Sans:ital,wght@0,400;0,600;0,700;1,400&display=swap" rel="stylesheet">
<style>
:root{
  --teal:#5fb3bd;
  --teal-dark:#4aa2ad;
  --ink:#222;
  --text:#6b6b6b;
  --light:#f3f3f3;
  --white:#fff;
  --dark:#2b2523;
  --red:#e0403f;
  --yellow:#f2b31c;
  --blue:#3aa6d8;
  --green:#7fbf4a;
}
*{margin:0;padding:0;box-sizing:border-box}
html,body{width:1200px;height:3536px;overflow:hidden}
body{font-family:"Open Sans",sans-serif;color:var(--text);background:var(--white);position:relative}
section,header,footer{position:absolute;left:0;width:1200px}
.abs{position:absolute}
h2{font-family:"Raleway",sans-serif;font-weight:700;color:var(--ink);font-size:30px;letter-spacing:.5px}
p{font-size:13px;line-height:25px}
.btn{position:absolute;display:flex;align-items:center;justify-content:center;border-radius:24px;font-family:"Raleway",sans-serif;font-weight:700;font-size:14px;color:var(--white);background:var(--teal);letter-spacing:.5px}

/* header */
.site-header{top:0;height:120px;background:var(--white)}
.brand{left:100px;top:20px;display:flex;flex-direction:column;align-items:center}
.brand-dot{width:56px;height:56px;border-radius:50%;background:#8a8f96}
.brand-name{font-family:"Raleway",sans-serif;font-weight:600;font-size:15px;color:#555;letter-spacing:2px;margin-top:6px}
.nav{left:340px;top:46px;display:flex;gap:0}
.nav a{font-family:"Raleway",sans-serif;font-weight:600;font-size:13px;color:var(--ink);text-decoration:none;position:absolute;white-space:nowrap}

/* hero */
.hero{top:120px;height:660px}
.hero-photo{left:0;top:0;width:1200px;height:630px;background:linear-gradient(110deg,#3a2a24 0%,#6d4a3a 35%,#a0705a 55%,#5a3d33 80%,#2e2420 100%)}
.hero-curve{left:0;top:380px}
.hero-title{left:100px;top:175px;font-family:"Raleway",sans-serif;font-weight:200;font-size:92px;letter-spacing:14px;color:var(--white)}
.hero-sub{left:100px;top:300px;font-size:23px;line-height:44px;color:var(--white)}
.btn-vip{left:100px;top:407px;width:128px;height:43px}
.btn-business{left:245px;top:407px;width:160px;height:43px;background:transparent;border:2px solid var(--white)}
.hero-device{left:895px;top:70px;width:205px;height:585px;border-radius:34px;background:linear-gradient(180deg,#e9e3e3,#cfc7c8);border:3px solid #d8cfd0}

/* welcome */
.welcome{top:780px;height:460px}
.welcome-screen{left:100px;top:75px;width:420px;height:280px;background:linear-gradient(180deg,#2b3440 0%,#dfe6ee 30%,#e9edf2 100%);border:8px solid #111;border-radius:4px}
.welcome h2{position:absolute;left:603px;top:75px}
.welcome p{position:absolute;left:603px;top:125px;width:495px}
.btn-more{width:150px;height:44px;font-size:13px}

/* what we do */
.what{top:1240px;height:500px}
.what-left{left:0;top:0;width:600px;height:500px;background:var(--light)}
.what-photo{left:600px;top:0;width:600px;height:500px;background:linear-gradient(135deg,#3c3a36 0%,#6f6359 45%,#a79a8b 70%,#4d4842 100%)}
.what h2{position:absolute;left:100px;top:62px}
.what .p1{position:absolute;left:100px;top:130px;width:470px}
.what .p2{position:absolute;left:100px;top:228px;width:470px}

/* benefits */
.benefits{top:1740px;height:525px;background:var(--teal)}
.benefits-photo{left:100px;top:90px;width:412px;height:345px;background:linear-gradient(135deg,#d9d2c8,#b8a58f 50%,#e6e1d8)}
.benefits-card{left:442px;top:112px;width:658px;height:306px;background:var(--white)}
.benefits-card h3{position:absolute;left:73px;top:27px;font-family:"Raleway",sans-serif;font-weight:700;font-size:20px;color:var(--ink)}
.benefit{position:absolute;top:75px;width:190px;text-align:center}
.benefit svg{display:block;margin:0 auto}
.benefit span{display:block;font-size:12.5px;line-height:19px;color:#333;margin-top:10px}
.arrow{position:absolute;top:140px}

/* how it works */
.how{top:2265px;height:550px}
.how-box{left:100px;top:120px;width:560px;height:315px;background:#eeeeee}
.how-box-inner{position:absolute;left:15px;top:15px;width:530px;height:285px;border:2px dashed #555}
.how h2{position:absolute;left:58px;top:50px;font-size:22px}
.how-lead{position:absolute;left:58px;top:88px;width:420px;font-size:13px;line-height:25px;color:#555}
.how-list{position:absolute;left:58px;top:148px;font-size:12px;color:#444;line-height:25px}
.how-list span{display:inline-block;width:135px}
.btn-video{left:58px;top:206px;width:145px;height:33px;font-size:12px;justify-content:flex-start;padding-left:14px}
.btn-video i{position:absolute;right:6px;top:6px;width:21px;height:21px;border-radius:50%;background:var(--white)}
.how-frame{left:580px;top:100px;width:520px;height:355px;border:2px solid var(--teal)}
.how-photo{position:absolute;left:6px;top:6px;width:504px;height:339px;background:linear-gradient(135deg,#2c5a63 0%,#3d6b72 40%,#8b9fa2 70%,#2f4548 100%)}

/* case study */
.case{top:2815px;height:400px;background:linear-gradient(180deg,#3a2f2c,#1f1a18 60%,#2b2220)}
.case h2{position:absolute;left:0;top:75px;width:1200px;text-align:center;color:var(--white);font-weight:600}
.legend{position:absolute;font-size:12px;color:var(--white);display:flex;align-items:center;gap:8px}
.legend i{width:14px;height:14px;border-radius:50%;display:inline-block}
.stars{left:258px;top:275px;color:var(--yellow);font-size:18px;letter-spacing:1px}
.count{left:258px;top:302px;font-size:17px;color:var(--white)}
.quote{left:600px;top:170px;width:505px;font-size:12px;line-height:25px;font-style:italic;color:var(--white)}
.author{left:945px;top:278px;font-family:"Raleway",sans-serif;font-weight:700;font-size:15px;color:var(--white)}
.author small{display:block;font-family:"Open Sans",sans-serif;font-weight:600;font-size:11px;margin-top:8px;margin-left:0}

/* contact */
.contact{top:3215px;height:245px;background:#f6f6f6}
.contact h2{position:absolute;left:100px;top:65px;font-size:19px}
.c-item{position:absolute;font-size:12px;line-height:24px;color:#555;padding-left:30px}
.c-item svg{position:absolute;left:0;top:6px}
.social{position:absolute;top:126px;width:38px;height:38px;border-radius:50%;border:1px solid #ccc;background:var(--white)}

/* footer */
.site-footer{top:3460px;height:76px;border-top:1px solid #ddd;background:var(--white)}
.site-footer p{text-align:center;font-size:12px;color:#555;margin-top:24px}
</style>
</head>
<body>

<header class="site-header">
  <div class="brand abs"><span class="brand-dot"></span><span class="brand-name">TOVRENDIX</span></div>
  <nav class="nav abs">
    <a style="left:0">WHAT WE DO</a>
    <a style="left:143px">BENEFITS</a>
    <a style="left:258px">TESTIMONIALS</a>
    <a style="left:408px">HOW IT WORKS</a>
    <a style="left:563px">CASE STUDY</a>
    <a style="left:698px">CONTACT</a>
  </nav>
</header>

<section class="hero">
  <div class="hero-photo abs" role="img" aria-label="Couple smiling while shopping and looking at a phone"></div>
  <svg class="hero-curve abs" width="1200" height="280" viewBox="0 0 1200 280"><path d="M0 220 C 300 280 750 270 1200 80 L1200 280 L0 280 Z" fill="#fff"/></svg>
  <div class="hero-title abs">TOVRENDIX</div>
  <div class="hero-sub abs">Tovrendix exceeds all expectations for<br>Shopping Centre Managers,Shoppers, Tenants and Landlords</div>
  <a class="btn btn-vip">VIP LOGIN</a>
  <a class="btn btn-business">BUSINESS LOGIN</a>
  <div class="hero-device abs" role="img" aria-label="Smartphone showing the app menu with shop, work, health, travel, bills and auto tiles"></div>
</section>

<section class="welcome">
  <div class="welcome-screen abs" role="img" aria-label="Desktop monitor showing the analytics dashboard"></div>
  <h2>WELCOME TO TOVRENDIX</h2>
  <p>Lorem ipsum dolor sit amet, consectetur adipiscing elit, sed do eiusmod tempor incididunt ut labore et dolore magna aliqua. Ut enim ad minim veniam, nostrud exercitation ullamco laboris nisi ut aliquip ex ea commodo consequat. Duis aute dolor in reprehenderit in voluptate velit esse cillum dolore&nbsp; fugiat nullapariatur perspiciatis unde omnis iste natus error sit voluptatem accusantium doloremque laudantium, totam rem aperiam,</p>
  <a class="btn btn-more" style="left:600px;top:310px">READ MORE &gt;&gt;</a>
</section>

<section class="what">
  <div class="what-left abs"></div>
  <div class="what-photo abs" role="img" aria-label="Developers working at computers with code on screen"></div>
  <h2>WHAT WE DO</h2>
  <p class="p1">Tovrendix provides shopping centre managers with an easy to use platform which enables them to delight their shoppers, impress their tenants, provide detailed data to their landlords and all accessible to them at the click of button.</p>
  <p class="p2">Tovrendix gives shopping centres real time tracking through smart ID's of individual customer journeys through their physical stores, enabling highly targeted, relevant and timely promotional and rewarding capabilities. Furthermore, through deep analytical data processing of the customer journey, centre managers will be able to more accurately and reliably predict shopping behaviours.</p>
  <a class="btn btn-more" style="left:97px;top:385px">READ MORE &gt;&gt;</a>
</section>

<section class="benefits">
  <div class="benefits-photo abs" role="img" aria-label="Happy couple looking at a phone in a shopping centre"></div>
  <div class="benefits-card abs">
    <h3>BENEFITS</h3>
    <svg class="arrow" style="left:14px" width="14" height="24" viewBox="0 0 14 24"><path d="M12 2 L3 12 L12 22" fill="none" stroke="#555" stroke-width="2"/></svg>
    <div class="benefit" style="left:28px">
      <svg width="150" height="150" viewBox="0 0 150 150"><circle cx="75" cy="75" r="68" fill="none" stroke="var(--teal)" stroke-width="6"/><circle cx="75" cy="75" r="52" fill="#eef7f8" role="img" aria-label="Server stack icon"/></svg>
      <span>Easy to install,<br>no wiring required</span>
    </div>
    <div class="benefit" style="left:235px">
      <svg width="150" height="150" viewBox="0 0 150 150"><circle cx="75" cy="75" r="68" fill="none" stroke="var(--teal)" stroke-width="6"/><circle cx="75" cy="75" r="52" fill="#fbecec" role="img" aria-label="Report document icon"/></svg>
      <span>Easy to use dashboard<br>with one click reporting</span>
    </div>
    <div class="benefit" style="left:443px">
      <svg width="150" height="150" viewBox="0 0 150 150"><circle cx="75" cy="75" r="68" fill="none" stroke="var(--teal)" stroke-width="6"/><circle cx="75" cy="75" r="52" fill="#eef3f6" role="img" aria-label="Cloud backup icon"/></svg>
      <span>Have the data to back up<br>any decision's you make</span>
    </div>
    <svg class="arrow" style="left:632px" width="14" height="24" viewBox="0 0 14 24"><path d="M2 2 L11 12 L2 22" fill="none" stroke="#555" stroke-width="2"/></svg>
  </div>
</section>

<section class="how">
  <div class="how-frame abs"><div class="how-photo" role="img" aria-label="Hand holding a phone displaying a discount code"></div></div>
  <div class="how-box abs">
    <div class="how-box-inner">
      <h2>HOW IT WORKS</h2>
      <p class="how-lead">sed quia non numquam eius modi tempora incidunt ut labore et dolore magnam aliquam quaerat voluptatem</p>
      <div class="how-list">
        <span>1. Allocate Cards</span><span>2. Direct Marketing</span><span>3. Rewarding Loyalty</span><br>
        <span>4. Collect data</span><span>5. Data Analytics</span>
      </div>
      <a class="btn btn-video">WATCH VIDEO <i></i></a>
    </div>
  </div>
</section>

<section class="case">
  <h2>CASE STUDY &amp; TESTIMONIAL</h2>
  <svg class="abs" style="left:48px;top:225px" width="16" height="30" viewBox="0 0 16 30"><path d="M14 2 L3 15 L14 28" fill="none" stroke="#fff" stroke-width="3"/></svg>
  <svg class="abs" style="left:1136px;top:225px" width="16" height="30" viewBox="0 0 16 30"><path d="M2 2 L13 15 L2 28" fill="none" stroke="#fff" stroke-width="3"/></svg>
  <svg class="abs" style="left:95px;top:160px" width="150" height="150" viewBox="0 0 150 150">
    <g transform="rotate(-90 75 75)" fill="none" stroke-width="46">
      <circle cx="75" cy="75" r="52" pathLength="100" stroke="var(--red)" stroke-dasharray="46 54" stroke-dashoffset="-54"/>
      <circle cx="75" cy="75" r="52" pathLength="100" stroke="var(--yellow)" stroke-dasharray="12 88" stroke-dashoffset="0"/>
      <circle cx="75" cy="75" r="52" pathLength="100" stroke="var(--blue)" stroke-dasharray="6 94" stroke-dashoffset="-12"/>
      <circle cx="75" cy="75" r="52" pathLength="100" stroke="#e07a3f" stroke-dasharray="16 84" stroke-dashoffset="-18"/>
      <circle cx="75" cy="75" r="52" pathLength="100" stroke="var(--green)" stroke-dasharray="20 80" stroke-dashoffset="-34"/>
    </g>
    <circle cx="75" cy="75" r="27" fill="#231d1b"/>
    <g font-family="Open Sans, sans-serif" font-weight="700" font-size="13" fill="#fff">
      <text x="10" y="80">49%</text><text x="55" y="30">16%</text><text x="85" y="30">6%</text>
      <text x="112" y="62">22%</text><text x="95" y="122">32%</text>
    </g>
  </svg>
  <div class="legend abs" style="left:258px;top:173px"><i style="background:var(--red)"></i>Doloremque laudantium</div>
  <div class="legend abs" style="left:435px;top:173px"><i style="background:var(--yellow)"></i>Nulla pariatur</div>
  <div class="legend abs" style="left:258px;top:203px"><i style="background:var(--blue)"></i>Excepteur sint</div>
  <div class="legend abs" style="left:435px;top:203px"><i style="background:var(--red)"></i>Occaecat cupidatat</div>
  <div class="legend abs" style="left:258px;top:233px"><i style="background:var(--green)"></i>Fugiat nulla pariatur</div>
  <div class="stars abs">★★★★★</div>
  <div class="count abs">15968</div>
  <p class="quote abs">"Sed ut perspiciatis unde omnis iste natus error sit voluptatem accusantium doloremque laudantium, totam rem aperiam, eaque ipsa quae ab illo inventore veritatis et quasi architecto beatae vitae dicta sunt explicabo nemo enim ipsam voluptatem quia voluptas sit aspernatur aut odit aut fugit"</p>
  <div class="author abs">- Author Name<small>City Location</small></div>
</section>

<section class="contact">
  <h2>CONTACT US</h2>
  <div class="c-item" style="left:100px;top:120px"><svg width="12" height="12" viewBox="0 0 12 12"><path d="M11 1 L1 5 L6 6 L7 11 Z" fill="#555"/></svg>Unit 7b, Harbour Road,<br>Carrow, CR12 4PL</div>
  <div class="c-item" style="left:100px;top:170px"><svg width="13" height="10" viewBox="0 0 13 10"><rect width="13" height="10" fill="#555"/><path d="M0 0 L6.5 6 L13 0" fill="none" stroke="#f6f6f6"/></svg>miles@tovrendix.com</div>
  <div class="c-item" style="left:275px;top:120px"><svg width="12" height="12" viewBox="0 0 12 12"><path d="M11 1 L1 5 L6 6 L7 11 Z" fill="#555"/></svg>Foundry, 3rd Floor 18 Mill Lane<br>Street , Ashby, AB4 2TN</div>
  <div class="c-item" style="left:275px;top:170px"><svg width="13" height="10" viewBox="0 0 13 10"><rect width="13" height="10" fill="#555"/><path d="M0 0 L6.5 6 L13 0" fill="none" stroke="#f6f6f6"/></svg>owen@tovrendix.com</div>
  <div class="c-item" style="left:527px;top:120px"><svg width="12" height="12" viewBox="0 0 12 12"><path d="M11 1 L1 5 L6 6 L7 11 Z" fill="#555"/></svg>2nd Floor, Weston House<br>Quay Street, Dunmore</div>
  <div class="c-item" style="left:527px;top:170px"><svg width="13" height="10" viewBox="0 0 13 10"><rect width="13" height="10" fill="#555"/><path d="M0 0 L6.5 6 L13 0" fill="none" stroke="#f6f6f6"/></svg>ruth@tovrendix.com</div>
  <div class="c-item" style="left:740px;top:120px"><svg width="12" height="12" viewBox="0 0 12 12"><path d="M2 1 L5 1 L6 4 L4 5 Q5 7 7 8 L8 6 L11 7 L11 10 Q5 11 1 4 Z" fill="#555"/></svg>Phone | 0415098732</div>
  <div class="c-item" style="left:740px;top:145px"><svg width="13" height="10" viewBox="0 0 13 10"><rect width="13" height="10" fill="#555"/><path d="M0 0 L6.5 6 L13 0" fill="none" stroke="#f6f6f6"/></svg>Email | hello@tovrendix.com</div>
  <span class="social" style="left:958px"></span>
  <span class="social" style="left:1010px"></span>
  <span class="social" style="left:1062px"></span>
</section>

<footer class="site-footer">
  <p>Copyright © Tovrendix 2018. All Rights Reserved.</p>
</footer>

</body>
</html>
```